Graphic works

Brief 1.
An Overview / Background of the Business & Services-
It is a new business being set up. Our business is to design a solution to enable Alumni of higher institutions in Nigeria apply for their academic transcript through our system. the name of our product will be Record Relay Nigeria. We need logo, site banner, advert banner and several academic images. See www.rvq-ng.example for more insight.
The Target Market / Audience you are trying to reach-
Alumni of Nigeria Universities, usually between the ages of 20-40.
Design Specifics; any preferences or ideas for Style, Colour, Imagery, etc-
Color scheme will be several shades of light blue and white. Please check www.rvq-ng.example for more insight.

Brief 2

Pantrybasket.example is an online food and grocery shop, we supply fresh food stuff and other daily essential needs on request to customers. The site is already up (www.pantrybasket.example). We need logo, site rolling banner, advert banner and several offer graphics as shown in the placeholder images in the site now.
Working women in Nigeria.
Color scheme will be several shades of light Green and White. Please check the site.

Colors
e9f1ce
33b7a4
add136
9bcb3c

```html
<!DOCTYPE html>
<html lang="en">
<head>
<meta charset="utf-8">
<title>Pantrybasket – Fresh Food Delivered</title>
<link href="https://fonts.googleapis.com/css2?family=Montserrat:wght@300;400;600&family=Open+Sans:wght@400;600&family=Oswald:wght@300;400;500;700&family=Arvo:wght@700&display=swap" rel="stylesheet">
<style>
  :root{
    --teal:#33b7a4;
    --lime:#add136;
    --leaf:#9bcb3c;
    --cream:#e9f1ce;
    --sky:#6bc8e0;
    --sky-deep:#44a9c8;
    --grey-bg:#b8c0c0;
    --ink:#555;
    --ink-soft:#6a6a6a;
    --rule:#e2e2e2;
    --frame:#ececec;
    --orange:#f7931e;
    --azure:#3aa0e0;
    --footer:#5a5a5a;
    --white:#fff;
  }
  *{margin:0;padding:0;box-sizing:border-box}
  html,body{width:1200px;height:1069px;overflow:hidden;background:var(--grey-bg)}
  .stage{position:absolute;left:0;top:0;width:1420px;height:1265px;transform:scale(0.84507);transform-origin:0 0;font-family:"Open Sans",sans-serif;color:var(--ink)}
  .abs{position:absolute}
  .page{left:188px;top:0;width:1044px;height:1214px;background:var(--white)}

  .masthead{left:188px;top:0;width:1044px;height:172px;background:var(--teal)}
  .brand{left:232px;top:58px;font-family:"Oswald",sans-serif;font-weight:300;font-size:56px;color:var(--white);letter-spacing:2px;line-height:1;white-space:nowrap}
  .account-links{left:930px;top:40px;font-family:"Montserrat",sans-serif;font-weight:600;font-size:14px;color:var(--white);white-space:nowrap}
  .account-links span{margin:0 6px}
  .cart-icon{left:876px;top:36px}
  .main-nav{top:102px;font-family:"Montserrat",sans-serif;font-weight:600;font-size:17px;color:var(--white);white-space:nowrap}

  .hero{left:188px;top:172px;width:785px;height:380px;background:radial-gradient(circle at 45% 55%,#f4c430 0%,#e8742a 22%,#c8303c 38%,#9dbb45 55%,#3f6e1e 85%)}
  .promo-delivery{left:975px;top:172px;width:255px;height:190px;background:linear-gradient(180deg,#fbfbe8,var(--cream))}
  .promo-delivery .title{position:absolute;left:0;width:100%;top:14px;text-align:center;font-family:"Oswald",sans-serif;font-weight:500;font-style:italic;font-size:38px;letter-spacing:-0.5px;color:var(--orange);line-height:1.1;white-space:nowrap}
  .promo-delivery .sub{position:absolute;left:0;width:100%;top:62px;text-align:center;font-family:"Oswald",sans-serif;font-size:24px;color:var(--azure);letter-spacing:-0.5px;line-height:1.2;white-space:nowrap}
  .read-more{position:absolute;left:24px;top:134px;width:212px;height:46px;border-radius:23px;background:linear-gradient(180deg,#ff9a2b,#f25c05);border:2px solid #ffb45a;color:var(--white);font-family:"Oswald",sans-serif;font-size:22px;display:flex;align-items:center;justify-content:center;gap:10px}
  .promo-relax{left:980px;top:370px;width:250px;height:182px;background:linear-gradient(180deg,#f8f8ee,#efe9c8 70%,#e8d98a)}
  .promo-relax .title{position:absolute;left:0;width:100%;top:8px;text-align:center;font-size:22px;line-height:26px;color:#444}
  .promo-relax .scene{position:absolute;left:40px;top:70px;width:170px;height:112px;border-radius:50% 50% 0 0;background:radial-gradient(ellipse at 50% 70%,#e6c9a0,#f3eedd 75%)}

  .tab{width:218px;height:38px;color:var(--white);font-family:"Arvo",serif;font-weight:700;font-size:16px;line-height:38px;padding-left:9px;text-shadow:0 1px 0 rgba(0,0,0,.25);clip-path:polygon(0 0,94% 0,100% 50%,94% 100%,0 100%)}
  .tab-categories{left:214px;top:583px;background:var(--sky);border-bottom:3px solid var(--sky-deep)}
  .tab-cart{left:214px;top:877px;background:var(--leaf);border-bottom:3px solid #7aa82a}
  .category-list{left:224px;top:637px;width:198px;list-style:none}
  .category-list li{height:31px;line-height:31px;border-bottom:1px solid var(--rule);font-size:14px;color:var(--ink-soft);position:relative}
  .category-list li.more::after{content:"+";position:absolute;right:12px;top:-2px;font-size:18px;color:#888}
  .cart-empty{left:233px;top:936px;width:190px;font-size:14px;line-height:20px;color:var(--ink-soft)}

  .section-title{left:451px;top:594px;font-family:"Arvo",serif;font-weight:700;font-size:15px;color:#7ab317}
  .pager{left:1125px;top:594px}
  .product{top:645px;width:230px;height:315px;border:5px solid var(--frame);background:var(--white)}
  .product .badge{position:absolute;left:0;top:0}
  .product .photo{position:absolute;left:8px;top:50px;width:204px;height:122px}
  .product .name{position:absolute;left:0;width:100%;top:222px;text-align:center;font-size:15px;color:var(--ink-soft)}
  .product .price{position:absolute;left:0;width:100%;top:249px;text-align:center;font-size:17px;font-weight:600;color:var(--ink-soft)}

  .banner-strip{left:188px;top:1047px;width:1044px;height:167px;background:var(--lime)}
  .ship-head{left:432px;top:1090px;font-family:"Oswald",sans-serif;font-size:34px;line-height:1;color:var(--white)}
  .ship-sub{left:431px;top:1128px;font-family:"Montserrat",sans-serif;font-size:20px;color:var(--white)}
  .call-label{left:750px;top:1075px;font-family:"Montserrat",sans-serif;font-size:22px;color:var(--white)}
  .call-number{left:750px;top:1108px;font-family:"Oswald",sans-serif;font-size:46px;line-height:1.1;color:var(--white)}

  .legal{left:0;top:1214px;width:1420px;height:51px;background:var(--footer);color:#eee;font-size:12px;text-align:center;line-height:51px}
</style>
</head>
<body>
<div class="stage">
  <div class="abs page"></div>

  <header class="abs masthead"></header>
  <div class="abs brand">PANTRYBASKET</div>
  <svg class="abs cart-icon" width="30" height="28" viewBox="0 0 30 28" aria-hidden="true">
    <path d="M1 3h5l4 15h15l3-11H8" fill="none" stroke="#fff" stroke-width="2.2"/>
    <path d="M10 10h17M11 14h15M14 7v11M18 7v11M22 7v11" stroke="#fff" stroke-width="1.3"/>
    <circle cx="12" cy="23" r="2.3" fill="#fff"/><circle cx="23" cy="23" r="2.3" fill="#fff"/>
  </svg>
  <nav class="abs account-links">My Account<span>|</span>My Wishlist<span>|</span>Login</nav>
  <div class="abs main-nav" style="left:605px">All</div>
  <div class="abs main-nav" style="left:646px">Health &amp; Wellnedd</div>
  <div class="abs main-nav" style="left:820px">Fruits &amp; vegs</div>
  <div class="abs main-nav" style="left:948px">Poltry Meat &amp; Fish</div>
  <div class="abs main-nav" style="left:1114px">Recipes</div>

  <div class="abs hero" role="img" aria-label="Close-up photo of fresh fruit skewers with strawberries, grapes, orange and blackberries"></div>

  <aside class="abs promo-delivery">
    <div class="title">FREE DELIVERY</div>
    <div class="sub">On Orders Above N4,999</div>
    <div class="read-more">READ MORE
      <svg width="26" height="26" viewBox="0 0 26 26" aria-hidden="true"><circle cx="13" cy="13" r="11" fill="none" stroke="#fff" stroke-width="2.5"/><path d="M7 13h11M13 8l5 5-5 5" fill="none" stroke="#fff" stroke-width="2.5"/></svg>
    </div>
  </aside>
  <aside class="abs promo-relax">
    <div class="title">RELAX LET’S DO<br>THE SHOPPING</div>
    <div class="scene" role="img" aria-label="Photo of a woman relaxing in a bath with flower petals"></div>
  </aside>

  <div class="abs tab tab-categories">CATEGORIES</div>
  <ul class="abs category-list">
    <li>All</li>
    <li>Health &amp; Wellness</li>
    <li class="more">Fruits &amp; Vegs</li>
    <li class="more">Poultry, Meat &amp; Fish</li>
    <li class="more">Food Stuffs</li>
    <li>Recipes</li>
    <li class="more">Others</li>
  </ul>
  <div class="abs tab tab-cart">MY CART</div>
  <p class="abs cart-empty">You have no items in your shopping cart.</p>

  <h2 class="abs section-title">LATEST PRODUCTS</h2>
  <svg class="abs pager" width="44" height="18" viewBox="0 0 44 18" aria-hidden="true">
    <circle cx="9" cy="9" r="8.5" fill="#b5b5b5"/><path d="M11 5l-4 4 4 4" fill="none" stroke="#fff" stroke-width="2"/>
    <circle cx="33" cy="9" r="8.5" fill="#b5b5b5"/><path d="M31 5l4 4-4 4" fill="none" stroke="#fff" stroke-width="2"/>
  </svg>

  <article class="abs product" style="left:451px">
    <svg class="badge" width="56" height="56" viewBox="0 0 56 56" aria-hidden="true"><path d="M0 0h56L0 56z" fill="#e8e8e8"/><text x="10" y="34" transform="rotate(-45 18 28)" font-family="Open Sans,sans-serif" font-size="13" fill="#777">New</text></svg>
    <div class="photo" role="img" aria-label="Photo of a whole frozen tilapia fish" style="background:radial-gradient(ellipse 50% 30% at 50% 50%,#6f7a80,#a9b0b4 60%,#fff 62%)"></div>
    <div class="name">Frozen Tilapia (1kg)</div>
    <div class="price">₦1,000.00</div>
  </article>
  <article class="abs product" style="left:697px">
    <svg class="badge" width="56" height="56" viewBox="0 0 56 56" aria-hidden="true"><path d="M0 0h56L0 56z" fill="#e8e8e8"/><text x="10" y="34" transform="rotate(-45 18 28)" font-family="Open Sans,sans-serif" font-size="13" fill="#777">New</text></svg>
    <div class="photo" role="img" aria-label="Photo of three red snapper fish on ice" style="background:linear-gradient(180deg,#f1e6ea,#e79088 35%,#f4eef1 50%,#e5837c 70%,#efe6ea)"></div>
    <div class="name">Red Snapper (1kg)</div>
    <div class="price">₦1,000.00</div>
  </article>
  <article class="abs product" style="left:943px">
    <svg class="badge" width="56" height="56" viewBox="0 0 56 56" aria-hidden="true"><path d="M0 0h56L0 56z" fill="#e8e8e8"/><text x="10" y="34" transform="rotate(-45 18 28)" font-family="Open Sans,sans-serif" font-size="13" fill="#777">New</text></svg>
    <div class="photo" role="img" aria-label="Photo of a whole frozen croaker fish" style="background:radial-gradient(ellipse 50% 26% at 50% 48%,#8f9478,#c4c6b2 60%,#fff 62%)"></div>
    <div class="name">Frozen Croacker (1kg)</div>
    <div class="price">₦1,000.00</div>
  </article>

  <section class="abs banner-strip"></section>
  <div class="abs ship-head">FREE SHIPPING</div>
  <div class="abs ship-sub">on orders above N 4,999</div>
  <div class="abs call-label">Call</div>
  <div class="abs call-number">0700 555 0142</div>

  <footer class="abs legal">Copyright 2014 company name- Terms &amp; Conditions | Privacy Policy</footer>
</div>
</body>
</html>
```